Bed & Breakfast Business Card Design

Casa Mirador Bed & Breakfast is a private, adult-only, upscale retreat for guests vacationing or on business in the Atlanta area.

Event venue for weddings & retreats

Target Market(s)

Age 40+ couples, romantic get-aways, honeymoon, small weddings, business retreats

Industry/Entity Type

Business

Contact Information for Business Card

Casa Mirador Bed & Breakfast, LLC
7208 Bramwick Ferry Road
Larkspur Hollow, GA 39901
555-555-0193
www.CasaMiradorRetreat-example.com

```html
<!DOCTYPE html>
<html lang="en">
<head>
<meta charset="utf-8">
<title>Casa Mirador Bed &amp; Breakfast — Business Card</title>
<link rel="stylesheet" href="https://fonts.googleapis.com/css2?family=PT+Sans&family=Crimson+Text&display=swap">
<style>
  :root {
    --page: #ffffff;
    --sky-top: #aeb3c0;
    --sky-mid: #c9c6cc;
    --stucco: #e9dcd2;
    --ground: #e3d8d0;
    --haze: rgba(255, 255, 255, 0.35);
    --name-blue: #1f6fb2;
    --ink: #222226;
    --accent-tone: rgba(40, 40, 44, 0.55);
  }
  html, body {
    margin: 0;
    width: 1200px;
    height: 757px;
    overflow: hidden;
    background: var(--page);
  }
  .canvas {
    position: relative;
    width: 1200px;
    height: 757px;
  }
  .card-shadow {
    position: absolute;
    left: 330px;
    top: 640px;
    width: 300px;
    height: 60px;
    border-radius: 50%;
    background: rgba(0, 0, 0, 0.28);
    filter: blur(18px);
  }
  .card-shadow.right {
    left: 480px;
    width: 180px;
  }
  .card {
    position: absolute;
    left: 25px;
    top: 0;
    width: 1104px;
    height: 654px;
    overflow: hidden;
  }
  .property-photo {
    position: absolute;
    inset: 0;
    background:
      linear-gradient(var(--haze), var(--haze)),
      radial-gradient(ellipse 30% 25% at 30% 58%, rgba(255, 226, 190, 0.8), transparent 70%),
      linear-gradient(180deg, var(--sky-top) 0%, var(--sky-mid) 30%, var(--stucco) 55%, var(--ground) 100%);
  }
  .business-name {
    position: absolute;
    left: 32px;
    top: 112px;
    width: 1040px;
    margin: 0;
    text-align: center;
    white-space: nowrap;
    font-family: "PT Sans", sans-serif;
    font-weight: 400;
    font-size: 68px;
    line-height: 1;
    color: var(--name-blue);
  }
  .corner-accent {
    position: absolute;
    left: 8px;
    top: 264px;
    width: 530px;
    height: 381px;
    background: linear-gradient(135deg, var(--accent-tone), rgba(40, 40, 44, 0.15));
    clip-path: polygon(0 0, 100% 100%, 0 100%);
  }
  .contact {
    position: absolute;
    right: 50px;
    top: 428px;
    text-align: right;
    color: var(--ink);
  }
  .address {
    margin: 0;
    font-family: "PT Sans", sans-serif;
    font-size: 36px;
    line-height: 40px;
  }
  .website {
    margin: 12px 0 0;
    font-family: "Crimson Text", serif;
    font-size: 35px;
    line-height: 40px;
  }
</style>
</head>
<body>
  <div class="canvas">
    <div class="card-shadow"></div>
    <div class="card-shadow right"></div>
    <section class="card">
      <div class="property-photo" role="img" aria-label="Evening photo of the inn's stucco courtyard with arched porch, lit windows and pine trees"></div>

      <h1 class="business-name">Casa Mirador Bed &amp; Breakfast</h1>

      <div class="corner-accent" role="img" aria-label="Decorative diagonal accent in the lower left corner"></div>

      <div class="contact">
        <p class="address">LLC 7208 Bramwick Ferry Road Larkspur Hollow<br>GA 39901 555-555-0193</p>
        <p class="website">www.CasaMiradorRetreat-example.com</p>
      </div>
    </section>
  </div>
</body>
</html>
```